Music Festival in Colorado Needs Awesome Flier Design

We need an eye-catching & captivating flier design for an annual music festival in Denver, CO (USA). The festival features the best Colorado musicians within the genres of jam - funk - bluegrass - electronic - reggae - rock.

The design should look clean and professional while still being creative and unique. The past three years' flier designs are attached, as well as the logo and some other designs that match the aesthetic of what we're looking for.

This festival has a big element of Colorado pride so any

Target Market(s)

Hippies - live music enthusiasts - partiers. Ages 21 - 40.

Industry/Entity Type

Entertainment

Colors
0355a3
ec1f27
ffffff
fbed22

Requirements
Must have
• Attached design text.
Nice to have
• - Quality texture and psychedelic elements.
• - Colorado pride elements; color scheme (red, white, blue & yellow), flag, ect.
• - Nature elements are awesome but this is also a downtown festival so keep that in mind.
Should not have
• Cheesy artwork.

```html
<!DOCTYPE html>
<html lang="en">
<head>
<meta charset="utf-8">
<title>Granite Sounds – Colorado Music Festival 2018</title>
<link rel="stylesheet" href="https://fonts.googleapis.com/css2?family=Abril+Fatface&family=Archivo+Black&family=Baloo+2:wght@700&display=swap">
<style>
  :root {
    --bg-deep: #5e0f14;
    --bg-mid: #8a1c22;
    --bg-light: #a83038;
    --cream: #fbf3d8;
    --yellow: #f7e86a;
    --disc-light: #f6a8a0;
    --disc-mid: #ee8178;
    --disc-ink: #6e2226;
    --name-ink: #2b2121;
  }
  * { margin: 0; padding: 0; box-sizing: border-box; }
  html, body { width: 848px; height: 1200px; overflow: hidden; background: var(--bg-deep); }
  .flyer { position: relative; width: 848px; height: 1200px; overflow: hidden; }
  .backdrop {
    position: absolute; inset: 0;
    background:
      radial-gradient(ellipse at 30% 20%, var(--bg-light) 0%, transparent 55%),
      radial-gradient(ellipse at 75% 70%, var(--bg-light) 0%, transparent 50%),
      linear-gradient(160deg, var(--bg-mid) 0%, var(--bg-deep) 100%);
  }
  .lineup {
    position: absolute; top: 72px; left: 0; width: 848px;
    text-align: center;
    font-family: "Abril Fatface", serif;
    font-size: 42px; line-height: 51px;
    color: var(--cream);
    transform: rotate(-3deg);
    text-shadow: 0 2px 3px rgba(0,0,0,0.35);
  }
  .lineup .hl { color: var(--yellow); }
  .disc {
    position: absolute; left: 138px; top: 506px;
    width: 572px; height: 584px; border-radius: 50%;
    background: radial-gradient(circle at 45% 40%, var(--disc-light) 0%, var(--disc-mid) 100%);
  }
  .disc-text {
    position: absolute; left: 0; width: 848px; text-align: center;
    font-family: "Archivo Black", sans-serif;
  }
  .edition { top: 540px; font-size: 38px; color: var(--disc-ink); letter-spacing: 1px; }
  .fest-name { top: 620px; font-size: 84px; line-height: 98px; color: var(--name-ink); letter-spacing: -1px; }
  .tagline { top: 856px; font-size: 22px; color: var(--name-ink); letter-spacing: 3px; }
  .year { top: 900px; font-size: 64px; color: var(--disc-ink); letter-spacing: 24px; padding-left: 24px; }
  .dates { top: 978px; font-size: 38px; color: var(--disc-ink); }
  .venue {
    position: absolute; left: 56px; top: 1058px; width: 760px;
    font-family: "Baloo 2", sans-serif; font-weight: 700;
    font-size: 29px; line-height: 50px;
    color: var(--yellow);
    transform: rotate(-5deg); transform-origin: left top;
  }
</style>
</head>
<body>
  <main class="flyer">
    <div class="backdrop" role="img" aria-label="Deep red textured mountain range under a starry sky"></div>

    <section class="lineup">
      <div><span class="hl">Milo Harlan Band</span> . Allhands</div>
      <div>Orchestra . <span class="hl">Fault Theory</span> . The</div>
      <div>Copper Sprouts . <span class="hl">J-Rae &amp; The Summit</span> .</div>
      <div>Wapiti . <span class="hl">Helix Kin</span> . Altitude</div>
      <div>Ensemble . <span class="hl">Sunwashed</span> . Parasonics .</div>
      <div><span class="hl">Kaleido</span> . Clear Daze . <span class="hl">Switch</span></div>
      <div><span class="hl">Yard</span> . Orbits</div>
    </section>

    <div class="disc" role="img" aria-label="Pink moon disc with faint mountain peaks"></div>
    <div class="disc-text edition">6TH ANNUAL</div>
    <div class="disc-text fest-name">GRANITE<br>SOUNDS</div>
    <div class="disc-text tagline">COLORADO MUSIC FESTIVAL</div>
    <div class="disc-text year">2018</div>
    <div class="disc-text dates">MAY 11TH-18TH</div>

    <section class="venue">
      <div>Larkspur Yard 412 W. 27th Ave Denver, CO 80211</div>
      <div>Tickets &amp; More Info @ www.granitesoundsfest.com</div>
    </section>
  </main>
</body>
</html>
```